New Brochures to deliver confidence of our company to our customers

I would like to have new brochure to be used to distribute to our prospective customers besides the power point presentation. I like the powerpoint you did for us and would like to follow the direction that you have set up. I will attach a number of photos for you to include in our brochure for you to choose. I like the brochure to be modern and forward thinking but just practical. The brochure needs to have three languages which are English, Chinese and Japanese. Attaches is the power point that we like.

Target Market(s)

Multinational companies

Industry/Entity Type

Electronics

Colors

Designer to choose colors to be used in the design.

Requirements
Must have
• Feel lively and modern and yet giving people a sense of confidence. Highlighting the automation is important. Can let us know if you want more photos. The brochure will have three languages, namely english, japanese and chinese.

```html
<!DOCTYPE html>
<html lang="en">
<head>
<meta charset="utf-8">
<title>KVN Circuits Brochure Spread</title>
<link rel="stylesheet" href="https://fonts.googleapis.com/css2?family=Montserrat:wght@400;600;800&family=Noto+Sans+SC:wght@400;700&family=Noto+Sans+JP:wght@400;700&display=swap">
<style>
  :root {
    --backdrop: #eef0ee;
    --paper: #ffffff;
    --paper-shade: #e9eaea;
    --ink: #1c1f22;
    --ink-soft: #4a4f55;
    --rule: #3a3d40;
    --strip: #dcdedf;
    --band-deep: #06141c;
    --band-teal: #0f4a52;
    --accent: #2f9a5a;
    --caption: #0d2a2c;
  }
  * { margin: 0; padding: 0; box-sizing: border-box; }
  html, body { width: 1200px; height: 700px; overflow: hidden; }
  body { background: var(--backdrop); position: relative; font-family: "Montserrat", sans-serif; color: var(--ink); }

  .spread { position: absolute; left: 220px; top: 88px; width: 760px; height: 527px; display: flex; box-shadow: 0 6px 18px rgba(0,0,0,.18); }
  .page { position: relative; width: 380px; height: 100%; background: var(--paper); overflow: hidden; }
  .page--left { background: linear-gradient(90deg, var(--paper) 88%, var(--paper-shade)); }
  .page--right { background: linear-gradient(90deg, var(--paper-shade), var(--paper) 10%); }

  .page-strip { position: absolute; top: 30px; left: 0; right: 0; height: 10px; background: var(--strip); font-size: 4px; color: var(--ink-soft); display: flex; align-items: center; gap: 30px; padding: 0 20px; }
  .page--right .page-strip { justify-content: space-between; }

  .title { position: absolute; left: 60px; top: 88px; font-weight: 800; font-size: 19.5px; line-height: 1.2; letter-spacing: .3px; text-transform: uppercase; }

  .body-en { position: absolute; left: 60px; width: 318px; font-size: 5px; line-height: 1.5; text-align: justify; color: var(--ink); }
  .body-en--one { top: 210px; }
  .body-en--two { top: 270px; font-weight: 600; }

  .divider { position: absolute; left: 60px; top: 342px; width: 246px; height: 1px; background: var(--rule); }

  .body-zh { position: absolute; left: 40px; width: 300px; font-family: "Noto Sans SC", sans-serif; font-size: 6px; line-height: 1.6; color: var(--ink); }
  .body-zh--one { top: 352px; }
  .body-zh--two { top: 402px; }
  .body-zh h3 { font-size: 6px; font-weight: 700; margin-bottom: 2px; }

  .brand { position: absolute; top: 55px; right: 75px; display: flex; align-items: center; gap: 4px; font-weight: 800; font-size: 10px; color: var(--accent); }
  .brand-mark { width: 9px; height: 9px; background: var(--accent); }

  .body-ja { position: absolute; left: 20px; width: 340px; font-family: "Noto Sans JP", sans-serif; font-size: 5.4px; line-height: 1.6; color: var(--ink); }
  .body-ja--one { top: 112px; }
  .body-ja--two { top: 170px; }

  .photo { position: absolute; left: 20px; top: 264px; width: 275px; height: 170px; background: linear-gradient(135deg, #cfd3d4 0%, #8d9396 45%, #7a5a3a 70%, #4c4f52 100%); }
  .caption { position: absolute; left: 165px; top: 434px; width: 175px; height: 18px; background: var(--caption); color: #fff; font-size: 7px; display: flex; align-items: center; justify-content: center; letter-spacing: .3px; }

  .band { position: absolute; left: 0; right: 0; bottom: 0; height: 52px; background: linear-gradient(180deg, var(--band-deep), var(--band-teal) 60%, var(--band-deep)); }
</style>
</head>
<body>
  <main class="spread">
    <section class="page page--left">
      <div class="page-strip"><span>4 / 10</span><span>KVN Circuits Company Profile</span></div>
      <h1 class="title">Double<br>Layered and<br>Multi-Layered<br>Printed Circuit</h1>
      <p class="body-en body-en--one">We produce two sided and multi-layered circuit boards for our customers through our carefully approved printed circuit board makers, working with a number of trusted partners to deliver high quality results for every order, so each board meets the needs of our customers.</p>
      <p class="body-en body-en--two">Our investment and upgrade plan brings highly automated lines into every stage of work. Since 2016 we have added new machines for testing and drilling, so each board is checked by machine before it leaves the factory for our customers.</p>
      <div class="divider"></div>
      <p class="body-zh body-zh--one">我们通过严格认证的电路板制造商为客户生产双面及多层电路板，<br>与多家合作伙伴共同为客户提供高品质产品。<br>所有产品均经过自动化检测，确保每块电路板符合客户要求。</p>
      <div class="body-zh body-zh--two"><h3>我们的设备升级</h3><p>自二零一六年起，公司持续投资自动化生产与检测设备，<br>全面提升钻孔、测试及品质管理能力，<br>每块电路板出厂前均经过机器检测，为客户带来稳定品质。</p></div>
      <div class="band" role="img" aria-label="Dark teal band with glowing circuit traces"></div>
    </section>
    <section class="page page--right">
      <div class="page-strip"><span>KVN Circuits Company Profile</span><span>5 / 10</span></div>
      <div class="brand"><span class="brand-mark"></span><span>KVN</span></div>
      <p class="body-ja body-ja--one">当社は厳選された認定メーカーを通じて、両面および多層プリント基板を製造しています。<br>複数の信頼できるパートナーと協力し、高品質な製品をお客様にお届けしています。<br>すべての基板は出荷前に自動検査を受け、品質を確認しています。</p>
      <p class="body-ja body-ja--two">設備投資とアップグレード<br>二〇一六年以降、自動化された生産ラインと検査装置に継続して投資しています。<br>穴あけ、検査、品質管理の各工程を強化し、安定した品質を実現しています。</p>
      <div class="photo" role="img" aria-label="Photo of an automated CNC drilling machine in the factory"></div>
      <div class="caption">Veltra Drill / CNC设备</div>
      <div class="band" role="img" aria-label="Dark teal band with glowing circuit traces"></div>
    </section>
  </main>
</body>
</html>
```